Golf Charity Classic Tournament

We need an upscale golf flyer for a business related annual golf tournament at a local country club.

I attached our flyer from last year to give you an idea of the information.
This flyer is missing a sponsor area so please leave an area for our sponsor logos.

The name of the tournament is the BRV Pathfinders Charity Classic.

For flyer details...
BRV Pathfinders Charity Classic, 11am registration, noon shotgun, Monday, November 9th, Thornhaven Country Club, see address on attached flyer.

Cost/membership info? $175 per player, $350 for twosome, or $600 on a foursome

Charity or cause? The Open Green of Greater Dallas

Any other important details? New features: Leaderboard and Caddie Club Leave bottom area for white/blank for sponsors

Digital or print? Digital jpeg file, but will need printable as well.

We will need logos added to flyer upon request until our event.

Thank you.

Target Market(s)

25-55 Corporate and Finance professionals for a business golf tournament that partners with Open Green charity

Industry/Entity Type

Business

Font styles to use
Serif

Requirements
Nice to have
• The flyer should be bold and stand out...Looking for creative design in the layout, use of color and fonts.
Should not have
• Boring golf appeal

```html
<!DOCTYPE html>
<html lang="en">
<head>
<meta charset="utf-8">
<title>BRV Pathfinders Charity Classic</title>
<link rel="stylesheet" href="https://fonts.googleapis.com/css2?family=Playfair+Display:wght@400;600;700;800&display=swap">
<style>
  :root {
    --green-dark: #17602a;
    --green-deep: #0f4a1f;
    --green-mid: #2a7d36;
    --green-light: #8cc63f;
    --gold: #f0b51c;
    --white: #ffffff;
    --ink: #333333;
  }
  html, body {
    margin: 0;
    padding: 0;
    width: 750px;
    height: 1200px;
    overflow: hidden;
    background: var(--white);
  }
  .flyer {
    position: relative;
    width: 750px;
    height: 1200px;
    background: var(--white);
    font-family: "Playfair Display", Georgia, serif;
  }
  .hero-photo {
    position: absolute;
    left: 0; top: 0;
    width: 750px; height: 472px;
    background:
      radial-gradient(ellipse at 30% 25%, #dfe9cf 0%, rgba(223,233,207,0) 45%),
      linear-gradient(180deg, #9cbf6c 0%, #6fa043 40%, #4f8a2c 70%, #3f7724 100%);
  }
  .title-band {
    position: absolute;
    left: 0; top: 472px;
    width: 750px; height: 190px;
    background: linear-gradient(180deg, var(--green-mid) 0%, var(--green-dark) 55%, var(--green-deep) 100%);
    border-top: 6px solid var(--gold);
    border-bottom: 6px solid var(--gold);
    box-sizing: border-box;
    display: flex;
    flex-direction: column;
    justify-content: center;
    align-items: center;
    gap: 8px;
    color: var(--white);
    text-align: center;
  }
  .title-band h1 {
    margin: 0;
    font-weight: 800;
    font-size: 46px;
    line-height: 1.12;
    text-transform: uppercase;
  }
  .new-features {
    margin: 0;
    font-weight: 600;
    font-size: 19px;
    letter-spacing: 2px;
    text-transform: uppercase;
    color: var(--gold);
  }
  .event-details {
    position: absolute;
    left: 0; top: 682px;
    width: 750px;
    margin: 0;
    text-align: center;
    color: var(--green-dark);
    font-weight: 800;
    font-size: 28px;
    line-height: 1.25;
    text-transform: uppercase;
  }
  .event-url {
    position: absolute;
    left: 0; top: 800px;
    width: 750px;
    margin: 0;
    text-align: center;
    color: var(--green-light);
    font-weight: 800;
    font-size: 26px;
    text-transform: uppercase;
  }
  .pricing-band {
    position: absolute;
    left: 0; top: 862px;
    width: 750px; height: 128px;
    background: var(--green-light);
    color: var(--white);
    font-weight: 800;
    font-size: 27px;
    text-transform: uppercase;
    display: flex;
    flex-direction: column;
    justify-content: center;
    align-items: center;
    gap: 14px;
  }
  .pricing-row {
    display: flex;
    gap: 50px;
  }
  .sponsors-label,
  .charity-label {
    position: absolute;
    top: 1010px;
    margin: 0;
    font-size: 18px;
    color: var(--ink);
    text-decoration: underline;
  }
  .sponsors-label { left: 50px; }
  .charity-label { right: 38px; }
  .charity-partner {
    position: absolute;
    right: 30px; top: 1058px;
    width: 210px;
    display: flex;
    align-items: center;
    gap: 10px;
  }
  .charity-partner .mark {
    flex: none;
    width: 22px; height: 22px;
    border-radius: 50%;
    background: var(--green-mid);
  }
  .charity-partner .name {
    font-weight: 700;
    font-size: 20px;
    line-height: 1.15;
    color: var(--green-dark);
  }
</style>
</head>
<body>
  <div class="flyer">
    <div class="hero-photo" role="img" aria-label="Gloved hand placing a golf ball on a tee over green grass with an iron club beside it"></div>

    <header class="title-band">
      <h1>The BRV Pathfinders<br>Charity Classic</h1>
      <p class="new-features">New: Leaderboard &amp; Caddie Club</p>
    </header>

    <p class="event-details">11AM Registration, Noon Shotgun,<br>Monday, November 9th, Thornhaven<br>Country Club.</p>

    <p class="event-url">www.brvpathfinders.org/dfw/events</p>

    <section class="pricing-band">
      <div class="pricing-row">
        <span>$175 per player</span>
        <span>$350 for twosome</span>
      </div>
      <div>$600 on a foursome</div>
    </section>

    <p class="sponsors-label">Our Sponsors</p>
    <p class="charity-label">Charity Partner</p>

    <div class="charity-partner">
      <span class="mark"></span>
      <span class="name">The Open Green of Greater Dallas</span>
    </div>
  </div>
</body>
</html>
```